Stationary For Harbor Allies
Harbor Allies
Project: Stationary For Harbor Allies
Stationary For Harbor Allies - Consulting
Creative Brief
Professional
Lou Brannick
President
547 Marlow Ln Spring Branch, TX 78070
lbrannick@harborallies4.com
www.harborallies4.com
I will need letterhead and envelopes as well as business cards. Feel free to try different fonts.
quelnor42 quelnor42
Designers, Please focus more on the letterhead and envelopes than the business cards. Thanks!

```html
<!DOCTYPE html>
<html lang="en">
<head>
<meta charset="utf-8">
<title>Harbor Allies – Business Card</title>
<link href="https://fonts.googleapis.com/css2?family=Oswald:wght@500&family=Roboto:wght@400;500;700&display=swap" rel="stylesheet">
<style>
  :root {
    --page: #e6e8ec;
    --card-top: #f7f8fa;
    --card-top-edge: #e3e6eb;
    --brand-blue: #2c4f8e;
    --brand-blue-deep: #223f74;
    --logo-blue: #2d62b5;
    --silver-light: #f4f5f7;
    --silver-mid: #c9cdd3;
    --silver-dark: #9aa0a8;
    --icon-disc: #e9ecf1;
    --text-light: #ffffff;
    --text-soft: #dbe3f1;
    --text-grey: #5b6068;
    --social: #4a4f57;
  }
  * { box-sizing: border-box; margin: 0; padding: 0; }
  html, body { width: 1200px; height: 770px; overflow: hidden; }
  body {
    background: var(--page);
    font-family: "Roboto", Arial, sans-serif;
    position: relative;
  }
  .card {
    position: absolute;
    left: 100px; top: 102px;
    width: 1000px; height: 565px;
    border-radius: 10px;
    overflow: hidden;
    box-shadow: 0 14px 40px rgba(30, 40, 60, 0.22);
    background: var(--card-top);
  }
  .card-head {
    position: absolute; left: 0; top: 0;
    width: 100%; height: 205px;
    background: linear-gradient(180deg, var(--card-top) 0%, var(--card-top-edge) 100%);
    display: flex; align-items: center; justify-content: center; gap: 22px;
  }
  .brand-mark {
    width: 86px; height: 86px; border-radius: 50%;
    background: var(--logo-blue);
  }
  .brand-name {
    font-family: "Roboto", Arial, sans-serif;
    font-weight: 500;
    font-size: 60px;
    color: var(--logo-blue);
    letter-spacing: 0.5px;
    white-space: nowrap;
  }
  .contact-band {
    position: absolute; left: 0; top: 205px;
    width: 100%; height: 245px;
    background: linear-gradient(180deg, var(--brand-blue) 0%, var(--brand-blue-deep) 100%);
    border-top: 5px solid var(--silver-mid);
    border-bottom: 5px solid var(--silver-mid);
    display: flex;
  }
  .contact-item {
    flex: 1;
    display: flex; flex-direction: column; align-items: center;
    padding-top: 26px;
    color: var(--text-light);
    text-align: center;
    white-space: nowrap;
  }
  .icon-disc {
    width: 92px; height: 92px; border-radius: 50%;
    background: var(--icon-disc);
    border: 3px solid var(--silver-dark);
    display: flex; align-items: center; justify-content: center;
    margin-bottom: 20px;
  }
  .icon-disc svg { width: 50px; height: 50px; }
  .person-name {
    font-family: "Oswald", Arial, sans-serif;
    font-weight: 500;
    font-size: 38px;
    line-height: 1;
    letter-spacing: 0.5px;
    text-transform: uppercase;
  }
  .person-role {
    font-size: 13px; letter-spacing: 1.5px;
    text-transform: uppercase; color: var(--text-soft);
    margin-top: 6px;
  }
  .contact-line {
    font-size: 21px; line-height: 1.5;
    letter-spacing: 0.3px;
  }
  .card-foot {
    position: absolute; left: 0; top: 450px;
    width: 100%; height: 115px;
    background: linear-gradient(180deg, var(--silver-light) 0%, var(--silver-mid) 55%, var(--silver-light) 100%);
    display: flex; align-items: center;
    padding-left: 92px; gap: 44px;
  }
  .follow { color: var(--text-grey); }
  .follow-title {
    font-family: "Oswald", Arial, sans-serif;
    font-weight: 500; font-size: 28px; letter-spacing: 2px;
    line-height: 1;
  }
  .follow-sub {
    font-size: 11px; letter-spacing: 1.2px; margin-top: 5px;
  }
  .social-list { display: flex; gap: 22px; list-style: none; }
  .social-list li {
    width: 24px; height: 24px; border-radius: 3px;
    background: var(--social);
  }
</style>
</head>
<body>
  <main class="card" aria-label="Harbor Allies business card">
    <header class="card-head">
      <span class="brand-mark" aria-hidden="true"></span>
      <span class="brand-name">Harbor Allies</span>
    </header>

    <section class="contact-band">
      <div class="contact-item">
        <div class="icon-disc">
          <svg viewBox="0 0 50 50" aria-hidden="true">
            <circle cx="25" cy="17" r="9" fill="#2c4f8e"/>
            <path d="M8 44 C8 32 16 28 25 28 C34 28 42 32 42 44 Z" fill="#2c4f8e"/>
          </svg>
        </div>
        <div class="person-name">Lou Brannick</div>
        <div class="person-role">President</div>
      </div>

      <div class="contact-item">
        <div class="icon-disc">
          <svg viewBox="0 0 50 50" aria-hidden="true" fill="none" stroke="#2c4f8e" stroke-width="3">
            <circle cx="25" cy="25" r="19"/>
            <ellipse cx="25" cy="25" rx="8" ry="19"/>
            <line x1="6" y1="25" x2="44" y2="25"/>
            <path d="M9 15 H41 M9 35 H41"/>
          </svg>
        </div>
        <div class="contact-line">lbrannick@harborallies4.com</div>
        <div class="contact-line">www.harborallies4.com</div>
      </div>

      <div class="contact-item">
        <div class="icon-disc">
          <svg viewBox="0 0 50 50" aria-hidden="true">
            <rect x="14" y="4" width="22" height="42" rx="4" fill="#2c4f8e"/>
            <rect x="17" y="10" width="16" height="26" fill="#e9ecf1"/>
            <circle cx="25" cy="41" r="2.2" fill="#e9ecf1"/>
          </svg>
        </div>
        <div class="contact-line">014 562 3790</div>
        <div class="contact-line">014 562 3790</div>
      </div>
    </section>

    <footer class="card-foot">
      <div class="follow">
        <div class="follow-title">FOLLOW US</div>
        <div class="follow-sub">ON SOCIAL NETWORKS</div>
      </div>
      <ul class="social-list" aria-label="Social networks">
        <li></li><li></li><li></li><li></li>
      </ul>
    </footer>
  </main>
</body>
</html>
```